I need a simple infographic that describes the 4 basic elements of how to effectively create change.

The overall title (Gentle Pressure Relentlessly Applied) should be at the top of the infographic. Subtitle is: "Leading Change".
There are four steps:
1. Alignment- Agreement on Approach
2. Transparency- Metrics for Assurance
3. Skills- Training and Coaching
4. Integrity- Culture of Accountability

Target Market(s)

Business Leaders in a training workshop

Font styles to use
Serif

Requirements
Must have
• Here are the 4 elements of the Infographic: Please show them in order.
• 1. Agreement on Approach. (Alignment)
• 2. Metrics for Assurance (Transparency)
• 3. Training and Coaching (Skills)
• 4. Culture of Accountability (Integrity)
Nice to have
• Cool Graphics that depict the 4 steps.
Should not have
• Pictures.

```html
<!DOCTYPE html>
<html lang="en">
<head>
<meta charset="utf-8">
<title>Leading Change – Harlow Partners</title>
<link rel="stylesheet" href="https://fonts.googleapis.com/css2?family=Oswald:wght@500;600&family=Lato:wght@400;700;900&display=swap">
<style>
  :root {
    --page-bg: #c9c9d6;
    --brand-blue: #2fa8d8;
    --brand-blue-light: #5cc0e2;
    --night: #181628;
    --footer: #3a3a3c;
    --purple: #55338c;
    --purple-light: #613f98;
    --lime: #d3db45;
    --lime-light: #e7eb6d;
    --teal: #00cfa6;
    --teal-light: #52dec8;
    --white: #ffffff;
    --ink: #111111;
  }
  html, body {
    margin: 0;
    padding: 0;
    width: 1200px;
    height: 1200px;
    overflow: hidden;
    background: var(--page-bg);
  }
  .flyer {
    position: absolute;
    left: 190px;
    top: 20px;
    width: 858px;
    height: 1214px;
    transform: scale(0.9555);
    transform-origin: 0 0;
  }
  .flyer svg { display: block; }
  .brand-name { font-family: "Lato", sans-serif; font-weight: 700; font-size: 46px; fill: var(--white); letter-spacing: 1px; }
  .headline { font-family: "Oswald", sans-serif; font-weight: 600; font-size: 50px; fill: var(--white); }
  .subtitle { font-family: "Lato", sans-serif; font-weight: 900; font-size: 28px; fill: var(--ink); letter-spacing: 0.5px; }
  .step-number { font-family: "Oswald", sans-serif; font-weight: 600; font-size: 52px; fill: var(--white); }
  .step-title { font-family: "Lato", sans-serif; font-weight: 900; font-size: 20px; fill: var(--white); }
  .step-text { font-family: "Lato", sans-serif; font-weight: 400; font-size: 20px; fill: var(--white); }
  .contact { font-family: "Lato", sans-serif; font-weight: 400; font-size: 20px; fill: var(--brand-blue); }
</style>
</head>
<body>
<div class="flyer">
<svg width="858" height="1214" viewBox="0 0 858 1214" xmlns="http://www.w3.org/2000/svg">
  <defs>
    <linearGradient id="grad-alignment" x1="0" y1="0" x2="0" y2="1"><stop offset="0" stop-color="var(--brand-blue)"/><stop offset="1" stop-color="var(--brand-blue-light)"/></linearGradient>
    <linearGradient id="grad-transparency" x1="0" y1="0" x2="0" y2="1"><stop offset="0" stop-color="var(--purple-light)"/><stop offset="1" stop-color="var(--purple)"/></linearGradient>
    <linearGradient id="grad-integrity" x1="0" y1="0" x2="0" y2="1"><stop offset="0" stop-color="var(--lime)"/><stop offset="1" stop-color="var(--lime-light)"/></linearGradient>
    <linearGradient id="grad-skills" x1="0" y1="0" x2="0" y2="1"><stop offset="0" stop-color="var(--teal-light)"/><stop offset="1" stop-color="var(--teal)"/></linearGradient>
  </defs>

  <!-- header -->
  <rect class="header-band" x="0" y="0" width="858" height="127" fill="var(--brand-blue)"/>
  <circle cx="215" cy="64" r="32" fill="none" stroke="var(--white)" stroke-width="5"/>
  <text class="brand-name" x="270" y="80">HARLOW PARTNERS</text>

  <rect class="title-band" x="0" y="127" width="858" height="78" fill="var(--night)"/>
  <text class="headline" x="429" y="186" text-anchor="middle">GENTLE PRESSURE RELENTLESSLY APLIED</text>

  <rect class="subtitle-band" x="0" y="205" width="858" height="50" fill="var(--white)"/>
  <text class="subtitle" x="418" y="240" text-anchor="middle">LEADING CHANGE</text>

  <rect class="body-panel" x="0" y="255" width="858" height="842" fill="var(--night)"/>

  <!-- step panels -->
  <polygon class="panel-alignment" points="76,334 420,450 420,682 192,682" fill="url(#grad-alignment)"/>
  <polygon class="panel-transparency" points="780,334 436,450 436,682 666,682" fill="url(#grad-transparency)"/>
  <polygon class="panel-skills" points="436,694 666,694 780,1040 436,924" fill="url(#grad-skills)"/>
  <polygon class="panel-integrity" points="192,694 420,694 420,924 76,1040" fill="url(#grad-integrity)"/>

  <!-- centre hub -->
  <circle class="hub" cx="428" cy="685" r="135" fill="var(--white)" stroke="var(--brand-blue)" stroke-width="22"/>

  <!-- step 01 -->
  <text class="step-number" x="114" y="414">01</text>
  <circle cx="192" cy="452" r="37" fill="var(--white)"/>
  <g fill="none" stroke="var(--brand-blue)" stroke-width="4" stroke-linecap="round" stroke-linejoin="round">
    <path d="M168 446 l12 -8 h10 l8 6 l6 -4 h10 l12 8"/>
    <path d="M180 450 l14 12 c3 3 8 0 5 -4 M188 456 l10 8 c3 3 8 0 5 -4 M198 452 l10 8"/>
  </g>
  <text class="step-title" x="215" y="518">ALIGNMENT</text>
  <text class="step-text" x="215" y="538">Agreement On</text>
  <text class="step-text" x="215" y="558">Approach</text>

  <!-- step 02 -->
  <text class="step-number" x="740" y="414" text-anchor="end">02</text>
  <circle cx="665" cy="452" r="37" fill="var(--white)"/>
  <circle cx="659" cy="446" r="15" fill="none" stroke="var(--purple)" stroke-width="4"/>
  <line x1="670" y1="457" x2="684" y2="471" stroke="var(--purple)" stroke-width="7" stroke-linecap="round"/>
  <text class="step-title" x="529" y="518">TRANSPARENCY</text>
  <text class="step-text" x="529" y="538">Metrics For</text>
  <text class="step-text" x="529" y="558">Assurance</text>

  <!-- step 03 -->
  <text class="step-title" x="529" y="832">SKILLS</text>
  <text class="step-text" x="529" y="852">Training And</text>
  <text class="step-text" x="529" y="872">Coaching</text>
  <circle cx="670" cy="920" r="37" fill="var(--white)"/>
  <g fill="none" stroke="var(--teal)" stroke-width="3" stroke-linejoin="round">
    <rect x="651" y="900" width="38" height="30"/>
    <polyline points="657,922 666,912 674,918 683,906"/>
    <circle cx="662" cy="936" r="3"/><circle cx="672" cy="936" r="3"/><circle cx="682" cy="936" r="3"/>
  </g>
  <text class="step-number" x="738" y="998" text-anchor="end">03</text>

  <!-- step 04 -->
  <text class="step-title" x="221" y="833">INTEGRITY</text>
  <text class="step-text" x="221" y="853">Culture Of</text>
  <text class="step-text" x="221" y="873">Accountability</text>
  <circle cx="197" cy="920" r="37" fill="var(--white)"/>
  <g fill="none" stroke="var(--lime)" stroke-width="3" stroke-linecap="round" stroke-linejoin="round">
    <circle cx="186" cy="904" r="5"/>
    <path d="M186 909 v16 h10 v14 M186 914 l20 -10"/>
    <rect x="196" y="930" width="14" height="12"/>
  </g>
  <text class="step-number" x="114" y="998">04</text>

  <!-- footer -->
  <rect class="footer-band" x="0" y="1097" width="858" height="117" fill="var(--footer)"/>
  <g fill="var(--brand-blue)">
    <path d="M84 1125 a7 7 0 0 1 7 7 c0 5 -7 12 -7 12 s-7 -7 -7 -12 a7 7 0 0 1 7 -7z"/>
    <circle cx="84" cy="1176" r="8"/>
    <circle cx="580" cy="1134" r="8"/>
    <circle cx="580" cy="1155" r="8"/>
  </g>
  <circle cx="84" cy="1132" r="2.5" fill="var(--footer)"/>
  <text class="contact" x="100" y="1141">48 Alder Creek Rd, Millbrook,</text>
  <text class="contact" x="100" y="1161">NC 28700</text>
  <text class="contact" x="100" y="1182">(800) 555-0142</text>
  <text class="contact" x="600" y="1141">info@harlowpartners.net</text>
  <text class="contact" x="600" y="1162">www.harlowpartners.net</text>
</svg>
</div>
</body>
</html>
```